Lantern Petals Website v.1 - attract floral shop franchisees

I need a simple information website for my new business. We are a franchisor of flower shops. The overall purpose of the website is to promote the company and the service, especially to potential franchisees and retailers. Only about 4 pages are required including homepage, About, For Supermarkets, For Franchisees, and Contact. No special functions are required except the site will have two separate inquiry forms that must be filled out online and submitted via automated email. Similarly, an email form should be linked from the Contact page. I have a logo and business cards designed by CraftHarbor, and I would like the site to have a consistent color scheme and style. The key to design will be to express the joy and love associated with flowers and floral bouquets.
IMPORTANT - I will be exporting the website design to Pageloft CMS in a site hosted by NetMarlow. For smooth integration into PageLoft hosted by NetMarlow, the designer should build the site using a PageLoft-friendly format. Ideally, they should use HTML, CSS, and PHP. Creating a custom theme or using a page builder that exports to PageLoft-compatible files is best. This ensures the site can be easily imported and managed within PageLoft.

Target Market(s)

Potential franchisees (existing florists or creative types who might like to own a floral business) and supermarkets who might want us to run their floral department

Industry/Entity Type

Floral retailing

Coding

Coded - Design and coding required

Number of Pages Required

4 page

Requirements
Must have
• A brand theme that is beautiful, consistent throughout and builds on the logo design
Nice to have
• Show gender and ethnic diversity in customers and florists. Pictures of happy florists (for franchisees) and pictures of amazing floral department displays (for supermarkets)

```html
<!DOCTYPE html>
<html lang="en">
<head>
<meta charset="UTF-8">
<title>Lantern Petals</title>
<link href="https://fonts.googleapis.com/css2?family=Bebas+Neue&family=Poppins:wght@400;500&display=swap" rel="stylesheet">
<style>
  :root{
    --green:#0a8f3f;
    --orange:#f29a1f;
    --ink:#111111;
    --text:#222222;
    --muted:#8a8a8a;
    --card:#f5f4f1;
    --white:#ffffff;
  }
  *{margin:0;padding:0;box-sizing:border-box}
  html,body{width:1200px;height:675px;overflow:hidden;background:var(--white)}
  body{position:relative;font-family:'Poppins',sans-serif;color:var(--text)}
  .brand{position:absolute;left:100px;top:22px;display:flex;align-items:center;gap:8px}
  .brand-dot{width:22px;height:22px;border-radius:50%;background:var(--orange)}
  .brand-name{font-size:17px;font-weight:500;color:var(--orange)}
  .nav{position:absolute;top:26px;right:100px;display:flex;align-items:center}
  .nav a{font-size:15px;color:var(--text);text-decoration:none;margin-left:30px}
  .nav .nav-cta{background:var(--green);color:var(--white);padding:5px 13px;margin-left:40px;box-shadow:0 8px 16px rgba(0,0,0,.1)}
  .hero-photo{position:absolute;left:100px;top:95px;width:320px;height:522px;
    background:linear-gradient(170deg,#5d7f3e 0%,#8fa56a 30%,#e7c4b2 45%,#5c8a47 65%,#7fb0b3 85%,#3f6a32 100%);
    box-shadow:0 10px 24px rgba(0,0,0,.12)}
  .contact-line{position:absolute;left:460px;top:94px;display:flex;gap:22px;font-size:12px;color:var(--green)}
  .contact-line span{display:flex;align-items:center;gap:10px}
  .headline{position:absolute;left:460px;top:136px;font-family:'Bebas Neue',sans-serif;font-weight:400;font-size:74px;line-height:81px;color:var(--ink)}
  .headline .orange{color:var(--orange)}
  .headline .green{color:var(--green)}
  .intro{position:absolute;left:460px;top:297px;width:500px;font-size:15px;line-height:25px;color:var(--ink)}
  .actions{position:absolute;left:460px;top:385px;display:flex;align-items:center;gap:30px}
  .btn-primary{width:150px;height:37px;background:var(--green);color:var(--white);font-size:12px;display:flex;align-items:center;justify-content:center;box-shadow:0 8px 16px rgba(0,0,0,.12)}
  .link-arrow{display:flex;align-items:center;gap:12px;color:var(--green);font-size:12px;text-decoration:underline}
  .stats{position:absolute;right:100px;top:130px;text-align:right}
  .stat{height:111px}
  .stat-num{font-family:'Bebas Neue',sans-serif;font-size:31px;line-height:34px;color:var(--green)}
  .stat-num.orange{color:var(--orange)}
  .stat-label{font-size:15px;color:var(--text);margin-top:2px}
  .section-title{position:absolute;left:460px;top:472px;font-family:'Bebas Neue',sans-serif;font-weight:400;font-size:26px;color:#222}
  .features{position:absolute;left:460px;top:517px;width:640px;display:flex;gap:15px}
  .feature{flex:1;height:100px;background:var(--card);display:flex;align-items:center;padding:0 10px;gap:10px}
  .feature-img{width:80px;height:80px;flex:none}
  .feature-title{font-family:'Bebas Neue',sans-serif;font-size:21px;color:#222;line-height:22px}
  .feature-more{font-size:11px;color:var(--muted);margin-top:6px}
</style>
</head>
<body>
  <div class="brand">
    <div class="brand-dot"></div>
    <div class="brand-name">Lantern Petals</div>
  </div>

  <nav class="nav">
    <a href="#">About Us</a>
    <a href="#">For Supermarkets</a>
    <a href="#">For Franchisees</a>
    <a href="#" class="nav-cta">Contact</a>
  </nav>

  <div class="hero-photo" role="img" aria-label="Smiling florist outdoors carrying a large bucket of pastel flowers on her shoulder"></div>

  <div class="contact-line">
    <span>
      <svg width="13" height="13" viewBox="0 0 24 24" fill="none" stroke="var(--green)" stroke-width="2"><path d="M22 16.9v3a2 2 0 0 1-2.2 2 19.8 19.8 0 0 1-8.6-3.1 19.5 19.5 0 0 1-6-6A19.8 19.8 0 0 1 2.1 4.2 2 2 0 0 1 4.1 2h3a2 2 0 0 1 2 1.7c.1.9.4 1.8.7 2.7a2 2 0 0 1-.5 2.1L8 9.8a16 16 0 0 0 6 6l1.3-1.3a2 2 0 0 1 2.1-.4c.9.3 1.8.6 2.7.7a2 2 0 0 1 1.7 2z"/></svg>
      +10 555 0142 7
    </span>
    <span>
      <svg width="14" height="11" viewBox="0 0 24 18" fill="none" stroke="var(--green)" stroke-width="2"><rect x="1" y="1" width="22" height="16"/><path d="M1 1l11 9 11-9"/></svg>
      hello@lanternpetals.com
    </span>
  </div>

  <h1 class="headline">Discover the <span class="orange">Lantern</span><br><span class="green">Petals</span> difference.</h1>

  <p class="intro">Enjoy top-quality flowers with professional service at affordable prices. Join our franchise network for exceptional support and growth opportunities.</p>

  <div class="actions">
    <div class="btn-primary">Shop Now</div>
    <div class="link-arrow">Contact Us
      <svg width="16" height="8" viewBox="0 0 16 8" fill="none" stroke="var(--green)" stroke-width="1.6"><path d="M0 4h14M11 1l3 3-3 3"/></svg>
    </div>
  </div>

  <div class="stats">
    <div class="stat"><div class="stat-num">100+</div><div class="stat-label">Plants</div></div>
    <div class="stat"><div class="stat-num orange">5000+</div><div class="stat-label">Customers</div></div>
    <div class="stat"><div class="stat-num">30+</div><div class="stat-label">Deliveries</div></div>
  </div>

  <h2 class="section-title">Why choose us?</h2>

  <div class="features">
    <div class="feature">
      <div class="feature-img" role="img" aria-label="Colourful ranunculus flowers" style="background:linear-gradient(135deg,#e85a7a,#f4c23a 60%,#e9a0a8)"></div>
      <div><div class="feature-title">Quality</div><div class="feature-more">See more &gt;&gt;</div></div>
    </div>
    <div class="feature">
      <div class="feature-img" role="img" aria-label="Flower market stall with buckets of blooms" style="background:linear-gradient(160deg,#b6584a,#7c9a66 50%,#2f3b3a)"></div>
      <div><div class="feature-title">Opportunity</div><div class="feature-more">See more &gt;&gt;</div></div>
    </div>
    <div class="feature">
      <div class="feature-img" role="img" aria-label="Florist arranging a bouquet in a shop" style="background:linear-gradient(150deg,#5d7d45,#c9a58c 55%,#e8b7c0)"></div>
      <div><div class="feature-title">Support</div><div class="feature-more">See more &gt;&gt;</div></div>
    </div>
  </div>
</body>
</html>
```